SEO Company Needs a Professional, Bold Business Card Design

Kelvo SEO
2487 N Harlow Ave #315
Brenford, TX 79913
512-555-0184
http://www.kelvoseo-demo.com
Kelvo SEO is an internet marketing company specializing in SEO for higher-end businesses. We are looking for a professional and bold (edgy) design that communicates our forward thinking SEO strategies. Our typical client is a small to medium US business that has never had SEO work done on their website but does has active marketing. We want our business card design to instill confidence in our services through a professional and bold look. We we would also like the design elements to be in line with the services we offer - ranking client websites in the search engine results, namely Zarnix.
Design Specifics:
Card design should have square edges.
Design should be delivered in fully layered and editable PSD file. Designing in AI is fine but I need a PSD file in case we have any changes in contact information or need additional cards for employees.
The design should compliment the attached logo.
Company Name:
Kelvo SEO
Address:
2487 N Harlow Ave #315
Brenford, TX 79913
Personal Info:
Dorian Welk
Owner
dorian@kelvoseo-demo.com
Phone:
877-555-0139 (KELVO UP)
Website:
http://www.kelvoseo-demo.com
Slogan:
Could Your Website Be Generating More Business?
Target Market(s)
High-end business owners - doctors, lawyers, specialists, business owners doing 250k in profit.
Industry/Entity Type
Internet
Contact Information for Business Card
Company Name:
Kelvo SEO
Address:
2487 N Harlow Ave #315
Brenford, TX 79913
Personal Info:
Dorian Welk
Owner
dorian@kelvoseo-demo.com
Phone:
877-555-0139 (KELVO UP)
Website:
www.kelvoseo-demo.com
Slogan:
Requirements
Must have
- Card design should have square edges.
- Background should be WHITE only.
- Design should be delivered in fully layered and editable PSD file. Designing in AI is fine but I need a PSD file in case we have any changes in contact information or need additional cards for employees.

```html
<!DOCTYPE html>
<html lang="en">
<head>
<meta charset="utf-8">
<title>Kelvo SEO Business Card</title>
<link href="https://fonts.googleapis.com/css2?family=Open+Sans:ital,wght@0,400;0,600;0,700;1,700&display=swap" rel="stylesheet">
<style>
  :root {
    --canvas: #e9ecef;
    --card: #ffffff;
    --navy: #0f3a66;
    --navy-dark: #0b2d52;
    --sky: #4fb3e6;
    --accent-red: #e0312f;
    --ink-light: #ffffff;
    --ink-soft: #c9d8e8;
  }
  * { box-sizing: border-box; margin: 0; padding: 0; }
  html, body { width: 1200px; height: 865px; overflow: hidden; }
  body {
    background: var(--canvas);
    font-family: "Open Sans", Arial, sans-serif;
    position: relative;
  }
  .card {
    position: absolute;
    top: 284px;
    width: 520px;
    height: 297px;
    background: var(--card);
    box-shadow: 0 6px 18px rgba(0,0,0,0.18);
    overflow: hidden;
  }
  .card--front { left: 53px; }
  .card--back { left: 627px; }

  .brand {
    position: absolute;
    left: 0; right: 0;
    text-align: center;
  }
  .card--front .brand { top: 112px; }
  .card--back .brand { top: 46px; }
  .brand__name {
    display: inline-flex;
    align-items: center;
    gap: 10px;
    font-weight: 700;
    color: var(--navy);
    font-size: 44px;
    line-height: 1;
  }
  .card--back .brand__name { font-size: 38px; }
  .brand__dot {
    width: 18px; height: 18px;
    border-radius: 50%;
    background: var(--sky);
  }
  .brand__tagline {
    margin-top: 6px;
    font-size: 13px;
    font-weight: 700;
    letter-spacing: 2px;
    color: var(--accent-red);
    text-transform: uppercase;
  }
  .card--back .brand__tagline { font-size: 11px; }

  .band {
    position: absolute;
    left: 0; right: 0;
    top: 168px;
    height: 104px;
    background: linear-gradient(90deg, var(--navy-dark), var(--navy) 60%, var(--navy-dark));
    color: var(--ink-light);
  }
  .person {
    position: absolute;
    left: 64px;
    top: 36px;
  }
  .person__name { font-size: 14px; font-weight: 700; font-style: italic; line-height: 1.3; }
  .person__role { font-size: 12px; color: var(--ink-soft); margin-top: 2px; }

  .contact {
    position: absolute;
    left: 330px;
    top: 11px;
    list-style: none;
    font-size: 10.5px;
    line-height: 1.3;
  }
  .contact li { display: flex; align-items: flex-start; gap: 6px; margin-bottom: 2px; }
  .contact li:last-child { margin-bottom: 0; }
  .contact svg { flex: none; width: 9px; height: 9px; margin-top: 3px; fill: var(--sky); }
  .contact strong { font-weight: 700; }
</style>
</head>
<body>
  <section class="card card--front" aria-label="Card front">
    <div class="brand">
      <div class="brand__name"><span class="brand__dot"></span>Kelvo SEO</div>
      <div class="brand__tagline">Internet Marketing</div>
    </div>
  </section>

  <section class="card card--back" aria-label="Card back">
    <div class="brand">
      <div class="brand__name"><span class="brand__dot"></span>Kelvo SEO</div>
      <div class="brand__tagline">Internet Marketing</div>
    </div>
    <div class="band">
      <div class="person">
        <div class="person__name">Dorian Welk</div>
        <div class="person__role">Owner</div>
      </div>
      <ul class="contact">
        <li>
          <svg viewBox="0 0 10 10"><path d="M2 0.5 L3.8 2.6 L2.9 3.8 Q4 6 6.2 7.1 L7.4 6.2 L9.5 8 L8.3 9.5 Q3 9 0.5 1.7 Z"/></svg>
          <span><strong>877-555-0139</strong> (KELVO UP)</span>
        </li>
        <li>
          <svg viewBox="0 0 10 10"><path d="M5 0 A3.5 3.5 0 0 1 8.5 3.5 C8.5 6 5 10 5 10 C5 10 1.5 6 1.5 3.5 A3.5 3.5 0 0 1 5 0 Z M5 2.2 A1.3 1.3 0 1 0 5 4.8 A1.3 1.3 0 1 0 5 2.2 Z"/></svg>
          <span>2487 N Harlow Ave #315<br>Brenford, TX 79913</span>
        </li>
        <li>
          <svg viewBox="0 0 10 10"><path d="M0 2 H10 V8 H0 Z M0.8 2.6 L5 5.6 L9.2 2.6" stroke="#0f3a66" stroke-width="0.8"/></svg>
          <span>dorian@kelvoseo-demo.com</span>
        </li>
        <li>
          <svg viewBox="0 0 10 10"><circle cx="5" cy="5" r="4.6"/><path d="M0.5 5 H9.5 M5 0.5 V9.5 M5 0.5 Q2 5 5 9.5 M5 0.5 Q8 5 5 9.5" stroke="#0f3a66" stroke-width="0.6" fill="none"/></svg>
          <span>www.kelvoseo-demo.com</span>
        </li>
      </ul>
    </div>
  </section>
</body>
</html>
```